Limbwright Crew of Yuma Bill Board Design

We are a high class full service tree company who specializes in artistic thinning and shaping of trees in Arizona. We want to re brand our company to catch our audiences attention and hook them into calling our company on the spot. We’ve been in business for 30 years and have never truly branded our company. We want our shirts trucks and billboards to match as well as our mailing advertisement so our clientele can recognize us immediately. We are starting with our billboard first and will be following with truck and shirt designs next. Attached is a example of what we are looking for and what we’ve had designed so far. This just isn’t good enough and needs revamped if at all posssible.
- Stencil

```html
<!DOCTYPE html>
<html lang="en">
<head>
<meta charset="utf-8">
<title>Limbwright Crew of Yuma – Billboard</title>
<link rel="stylesheet" href="https://fonts.googleapis.com/css2?family=Alegreya+SC:wght@500&family=Alegreya:wght@400&family=Dancing+Script:wght@600&family=Oswald:wght@600;700&display=swap">
<style>
  :root {
    --page-bg: #5a5a5a;
    --board-white: #ffffff;
    --leaf-green: #0f9a1a;
    --deep-green: #0b8a15;
    --clay: #c0602a;
    --clay-pill: #c8683a;
    --ink: #1d1d1d;
    --photo-sand: #b7a48c;
    --photo-foliage: #5f7a3c;
    --photo-sky: #7da7d6;
  }
  * { margin: 0; padding: 0; box-sizing: border-box; }
  html, body { width: 955px; height: 1200px; overflow: hidden; background: var(--page-bg); }
  .billboard {
    position: absolute; left: 20px; top: 371px;
    width: 915px; height: 457px; overflow: hidden;
  }
  .billboard-inner {
    position: absolute; left: 0; top: 0;
    width: 1345px; height: 672px;
    transform: scale(0.6803); transform-origin: 0 0;
    background: var(--board-white);
  }
  .board-shapes { position: absolute; inset: 0; }
  .brand { position: absolute; left: 690px; top: 62px; display: flex; align-items: center; gap: 22px; }
  .brand-mark { width: 76px; height: 76px; border-radius: 50%; background: var(--leaf-green); flex: none; }
  .brand-name {
    font-family: "Alegreya SC", serif; font-weight: 500; font-size: 40px;
    color: var(--ink); line-height: 1; white-space: nowrap;
  }
  .tagline {
    position: absolute; left: 872px; top: 122px;
    font-family: "Dancing Script", cursive; font-weight: 600; font-size: 38px;
    color: var(--leaf-green); white-space: nowrap;
  }
  .headline {
    position: absolute; left: 650px; top: 236px;
    font-family: "Oswald", sans-serif; font-weight: 700; font-size: 62px;
    color: var(--clay); letter-spacing: -0.5px; white-space: nowrap;
    transform: scaleX(0.92); transform-origin: left center;
  }
  .service-list {
    position: absolute; top: 338px; list-style: none;
    font-family: "Alegreya", serif; font-size: 26px; color: var(--ink);
  }
  .service-list.col-a { left: 676px; }
  .service-list.col-b { left: 992px; }
  .service-list li { display: flex; align-items: center; gap: 10px; height: 47px; white-space: nowrap; }
  .tick { width: 18px; height: 18px; flex: none; }
  .estimate-pill {
    position: absolute; left: 851px; top: 526px; width: 298px; height: 30px;
    border-radius: 15px; background: var(--clay-pill);
    font-family: "Alegreya", serif; font-size: 18px; letter-spacing: 0.5px;
    color: #fff; text-align: center; line-height: 30px; text-transform: uppercase;
  }
  .phone { position: absolute; left: 712px; top: 565px; display: flex; align-items: center; gap: 12px; }
  .phone-icon { width: 70px; height: 70px; flex: none; }
  .phone-number {
    font-family: "Oswald", sans-serif; font-weight: 700; font-size: 92px;
    color: #fff; line-height: 1; letter-spacing: -1px;
    transform: scaleX(0.9); transform-origin: left center; white-space: nowrap;
  }
</style>
</head>
<body>
  <div class="billboard">
    <div class="billboard-inner">
      <svg class="board-shapes" viewBox="0 0 1345 672" width="1345" height="672">
        <defs>
          <linearGradient id="yard-photo" x1="0" y1="0" x2="0" y2="1">
            <stop offset="0" stop-color="var(--photo-foliage)"/>
            <stop offset="0.45" stop-color="#8d8173"/>
            <stop offset="1" stop-color="var(--photo-sand)"/>
          </linearGradient>
          <linearGradient id="canopy-photo" x1="0" y1="0" x2="1" y2="1">
            <stop offset="0" stop-color="var(--photo-sky)"/>
            <stop offset="0.5" stop-color="#5d8a45"/>
            <stop offset="1" stop-color="#2f5d8f"/>
          </linearGradient>
          <linearGradient id="divider" x1="0" x2="1">
            <stop offset="0" stop-color="var(--clay)" stop-opacity="0.1"/>
            <stop offset="0.5" stop-color="#8a5a1e"/>
            <stop offset="1" stop-color="var(--leaf-green)" stop-opacity="0.2"/>
          </linearGradient>
        </defs>
        <path role="img" aria-label="Photo of an arborist deep-watering a young tree in a gravel yard"
              d="M0 0 H522 C598 80 640 250 618 420 L600 620 H0 Z" fill="url(#yard-photo)"/>
        <path d="M527 0 C604 82 646 252 624 420 L612 520" fill="none" stroke="var(--leaf-green)" stroke-width="7"/>
        <path d="M0 535 C150 580 300 602 440 606" fill="none" stroke="var(--clay)" stroke-width="9"/>
        <path d="M0 552 C150 592 300 614 440 614 L640 560 C800 512 950 490 1050 492 C1200 496 1300 528 1345 548 V672 H0 Z"
              fill="var(--leaf-green)"/>
        <path d="M640 555 C760 520 860 500 960 494" fill="none" stroke="var(--board-white)" stroke-width="2"/>
        <line x1="765" y1="224" x2="1195" y2="224" stroke="url(#divider)" stroke-width="3"/>
        <circle cx="514" cy="506" r="130" fill="var(--board-white)"/>
        <circle role="img" aria-label="Photo of a worker pruning a tree from a bucket lift"
                cx="514" cy="506" r="124" fill="url(#canopy-photo)"/>
      </svg>

      <div class="brand">
        <span class="brand-mark"></span>
        <span class="brand-name">Limbwright Crew of Yuma</span>
      </div>
      <div class="tagline">Providing Expert Tree Care</div>

      <h1 class="headline">WE SCULPT TREES IN ARIZONA</h1>

      <ul class="service-list col-a">
        <li><svg class="tick" viewBox="0 0 18 18"><rect x="1" y="3" width="13" height="13" fill="none" stroke="var(--leaf-green)" stroke-width="2"/><path d="M4 9 L8 13 L17 2" fill="none" stroke="var(--leaf-green)" stroke-width="2.4"/></svg>Tree Trimming &amp; Pruning</li>
        <li><svg class="tick" viewBox="0 0 18 18"><rect x="1" y="3" width="13" height="13" fill="none" stroke="var(--leaf-green)" stroke-width="2"/><path d="M4 9 L8 13 L17 2" fill="none" stroke="var(--leaf-green)" stroke-width="2.4"/></svg>Tree Planting &amp; Fertilizing</li>
        <li><svg class="tick" viewBox="0 0 18 18"><rect x="1" y="3" width="13" height="13" fill="none" stroke="var(--leaf-green)" stroke-width="2"/><path d="M4 9 L8 13 L17 2" fill="none" stroke="var(--leaf-green)" stroke-width="2.4"/></svg>Tree Shaping</li>
      </ul>
      <ul class="service-list col-b">
        <li><svg class="tick" viewBox="0 0 18 18"><rect x="1" y="3" width="13" height="13" fill="none" stroke="var(--leaf-green)" stroke-width="2"/><path d="M4 9 L8 13 L17 2" fill="none" stroke="var(--leaf-green)" stroke-width="2.4"/></svg>Tree Trimming &amp; Pruning</li>
        <li><svg class="tick" viewBox="0 0 18 18"><rect x="1" y="3" width="13" height="13" fill="none" stroke="var(--leaf-green)" stroke-width="2"/><path d="M4 9 L8 13 L17 2" fill="none" stroke="var(--leaf-green)" stroke-width="2.4"/></svg>Tree Removal</li>
        <li><svg class="tick" viewBox="0 0 18 18"><rect x="1" y="3" width="13" height="13" fill="none" stroke="var(--leaf-green)" stroke-width="2"/><path d="M4 9 L8 13 L17 2" fill="none" stroke="var(--leaf-green)" stroke-width="2.4"/></svg>Certified Arborist</li>
      </ul>

      <div class="estimate-pill">Request a free estimate</div>

      <div class="phone">
        <svg class="phone-icon" viewBox="0 0 70 70">
          <circle cx="35" cy="35" r="31" fill="none" stroke="#fff" stroke-width="5"/>
          <path d="M24 19 L30 18 L33 27 L29 30 C31 36 34 39 40 41 L43 37 L52 40 L51 46 C50 50 46 52 42 51 C30 48 22 40 19 28 C18 24 20 20 24 19 Z" fill="#fff"/>
          <path d="M38 22 C43 23 47 27 48 32 M38 15 C46 16 54 24 55 32" fill="none" stroke="#fff" stroke-width="3"/>
        </svg>
        <span class="phone-number">480-555-0193</span>
      </div>
    </div>
  </div>
</body>
</html>
```